Business Card Design

An energy company designed around renewable energy and energy storage that focuses on providing its energy at points on the grid that reduce costs and add value to the system.

Industry/Entity Type

Business

Contact Information for Business Card

Martin Dellacroix
Executive Vice President
41 K ST NE
Washington, DC 20017
240-555-0187
mdellacroix@brightvaleenergy.example

```html
<!DOCTYPE html>
<html lang="en">
<head>
<meta charset="utf-8">
<title>Business Card – Martin Dellacroix</title>
<link rel="stylesheet" href="https://fonts.googleapis.com/css2?family=Roboto+Condensed:wght@400&display=swap">
<style>
  :root {
    --backdrop: #1b242b;
    --card: #ffffff;
    --ribbon-red: #ea1c24;
    --ribbon-fold: #8f1c1f;
    --ribbon-shadow: #e2e3e4;
    --name-white: #ffffff;
    --title-ink: #2b2222;
    --contact-grey: #8b8e91;
    --divider-salmon: #f1a184;
  }
  html, body {
    margin: 0;
    padding: 0;
    width: 1200px;
    height: 1000px;
    overflow: hidden;
    background: var(--backdrop);
    font-family: "Roboto Condensed", "Arial Narrow", sans-serif;
  }
  .business-card {
    position: absolute;
    left: 163px;
    top: 251px;
    width: 872px;
    height: 498px;
    background: var(--card);
  }
  .ribbon {
    position: absolute;
    left: 0;
    top: 0;
  }
  .identity {
    position: absolute;
    left: 40px;
    top: 91px;
    width: 320px;
  }
  .identity__name {
    margin: 0;
    font-size: 39px;
    font-weight: 400;
    line-height: 1;
    color: var(--name-white);
    padding-bottom: 10px;
    border-bottom: 1.5px solid var(--name-white);
    letter-spacing: 0.2px;
  }
  .identity__title {
    margin: 6px 0 0;
    font-size: 27px;
    line-height: 1.2;
    color: var(--title-ink);
  }
  .contact {
    position: absolute;
    left: 371px;
    top: 291px;
    height: 155px;
    padding-left: 20px;
    border-left: 2px solid var(--divider-salmon);
    display: flex;
    flex-direction: column;
    justify-content: center;
    gap: 5px;
  }
  .contact__line {
    margin: 0;
    font-size: 25px;
    line-height: 1.28;
    color: var(--contact-grey);
    white-space: nowrap;
  }
</style>
</head>
<body>
  <section class="business-card" aria-label="Business card for Martin Dellacroix">
    <svg class="ribbon" width="400" height="220" viewBox="0 0 400 220" aria-hidden="true">
      <polygon points="0,200 360,200 356,212 0,212" fill="var(--ribbon-shadow)"/>
      <polygon points="0,75 390,75 372,200 0,200" fill="var(--ribbon-red)"/>
      <polygon points="0,75 20,75 20,200 0,200" fill="var(--ribbon-fold)"/>
    </svg>

    <div class="identity">
      <h1 class="identity__name">Martin Dellacroix</h1>
      <p class="identity__title">Executive Vice President</p>
    </div>

    <div class="contact">
      <p class="contact__line">240-555-0187</p>
      <p class="contact__line">mdellacroix@brightvaleenergy.example</p>
      <p class="contact__line">41 K ST NE Washington, DC 20017</p>
    </div>
  </section>
</body>
</html>
```